POP ART / Benny Coltrane type advertisment for medical practice

Our medical practice would like an ad resembling "Pop Art" / Benny Coltrane artwork.
We like outside-the-box advertisements and DO NOT want to look like a doctor's office / hospital / healthcare facility ad. It would be good to have an ad that can be used for full page and a modified one that could be used for quarter page ads that doesn't sacrifice the artistic vision you have created!
Reason: Would like more designs! Thanks!
Target Market(s)
adults 18-100+
Industry/Entity Type
Healthcare
Colors
Designer to choose colors to be used in the design.
Requirements
Must have
- must have photo of Dr. Talbrun
- his name Otto Talbrun, MD
- the practice logo
- the address: 41857 Pelican Drive, Suite 270, Mission Viejo, CA 92784
- phone: 949-555-0173
- website: www.fenwoodclinic.example
- tag line: Modern Medicine, Traditional Care
Nice to have
- family practice
- open daily
- book online
Should not have
- look like a doctor office or healthcare facility ad

```html
<!DOCTYPE html>
<html lang="en">
<head>
<meta charset="UTF-8">
<title>Otto Talbrun, MD — Fenwood Medical Group</title>
<link rel="stylesheet" href="https://fonts.googleapis.com/css2?family=Arimo:wght@400;700&family=Roboto+Condensed:wght@700&display=swap">
<style>
  :root {
    --navy: #17233d;
    --red: #e0101a;
    --yellow: #f7e100;
    --portrait-light: #f7e100;
    --portrait-mid: #f0b400;
    --white: #ffffff;
    --backdrop: #ececec;
    --ink: #17233d;
  }
  * { margin: 0; padding: 0; box-sizing: border-box; }
  html, body { width: 1200px; height: 1200px; overflow: hidden; background: var(--backdrop); }
  .canvas { position: relative; width: 1200px; height: 1200px; }
  .poster {
    position: absolute; left: 220px; top: 68px;
    width: 758px; height: 1072px;
    background: var(--white);
    box-shadow: 0 2px 10px rgba(0,0,0,0.15);
  }
  .artwork {
    position: absolute; left: 21px; top: 28px;
    width: 716px; height: 948px; overflow: hidden;
  }
  .artwork-shapes { position: absolute; inset: 0; }
  .tagline {
    position: absolute; left: 14px; top: 13px;
    font-family: "Arimo", Arial, sans-serif; color: var(--white);
    font-size: 90px; line-height: 79px; letter-spacing: -1px;
  }
  .tagline .light { font-weight: 400; display: block; }
  .tagline .strong { font-weight: 700; display: block; }
  .doctor-name {
    position: absolute; left: 170px; top: 532px;
    transform-origin: 0 0; transform: rotate(-45deg);
    font-family: "Arimo", Arial, sans-serif; font-weight: 700;
    color: var(--white); font-size: 86px; line-height: 84px;
    white-space: nowrap;
  }
  .doctor-name .credential { display: block; padding-left: 36px; }
  .booking {
    position: absolute; left: 14px; top: 705px;
    font-family: "Roboto Condensed", "Arial Narrow", sans-serif; font-weight: 700;
    color: var(--navy); font-size: 114px; line-height: 102px;
  }
  .website {
    position: absolute; left: 16px; top: 900px;
    font-family: "Arimo", Arial, sans-serif; color: var(--navy); font-size: 36px; line-height: 40px;
  }
  .footer { position: absolute; left: 21px; top: 976px; width: 716px; height: 96px; }
  .brand { position: absolute; left: 0; top: 20px; display: flex; align-items: center; gap: 8px; }
  .brand-mark { width: 42px; height: 42px; background: var(--ink); }
  .brand-name {
    font-family: "Arimo", Arial, sans-serif; font-weight: 700; color: var(--ink);
    font-size: 26px; line-height: 26px;
  }
  .brand-sub { display: block; font-size: 11px; line-height: 16px; letter-spacing: 4.6px; }
  .contact { position: absolute; left: 325px; top: 18px; font-family: "Arimo", Arial, sans-serif; color: #111; }
  .phone { font-size: 24px; line-height: 30px; }
  .address { font-size: 14.5px; line-height: 20px; }
</style>
</head>
<body>
<div class="canvas">
  <div class="poster">
    <div class="artwork">
      <svg class="artwork-shapes" width="716" height="948" viewBox="0 0 716 948" aria-hidden="true">
        <defs>
          <radialGradient id="portraitGlow" cx="0.5" cy="0.42" r="0.5">
            <stop offset="0" stop-color="var(--portrait-light)"/>
            <stop offset="0.45" stop-color="var(--portrait-mid)"/>
            <stop offset="1" stop-color="var(--red)" stop-opacity="0"/>
          </radialGradient>
          <clipPath id="redArea">
            <polygon points="716,0 716,948 648,948 205,505"/>
          </clipPath>
        </defs>
        <rect width="716" height="948" fill="var(--red)"/>
        <polygon points="0,0 716,0 0,710" fill="var(--navy)"/>
        <polygon points="0,710 205,505 648,948 0,948" fill="var(--yellow)"/>
      </svg>
      <svg class="artwork-shapes" width="716" height="948" viewBox="0 0 716 948" role="img" aria-label="Pop art halftone portrait of Dr. Talbrun in yellow and red">
        <g clip-path="url(#redArea)">
          <ellipse cx="545" cy="640" rx="190" ry="330" fill="url(#portraitGlow)"/>
        </g>
      </svg>
      <h1 class="tagline">
        <span class="light">Modern</span>
        <span class="light">Medicine,</span>
        <span class="strong">Traditional</span>
        <span class="strong">Care</span>
      </h1>
      <div class="doctor-name">Otto Talbrun,<span class="credential">MD</span></div>
      <div class="booking">Book<br>Online at</div>
      <div class="website">www.fenwoodclinic.example</div>
    </div>
    <div class="footer">
      <div class="brand">
        <span class="brand-mark"></span>
        <span class="brand-name">Fenwood<span class="brand-sub">MEDICAL GROUP</span></span>
      </div>
      <div class="contact">
        <div class="phone">949-555-0173</div>
        <div class="address">41857 Pelican Drive, Suite 270, Mission Viejo, CA 92784</div>
      </div>
    </div>
  </div>
</div>
</body>
</html>
```